Design my dad a new business card because his current one sucks!

I need a business card designed for my fathers home maintenance business. His customers are individuals (single moms, old people etc.) as well as the occasional business. As such it needs to be accessible to both target audiences.

The front of the card should be dark grey on yellow with the logo and contain the following information:
- Warren Dobrinski
- 0487 362 914
- info@harbourlinehandyworks.com.au
- 0487 362 914

- ABN: 87 214 630 592
- 'Fully Insured'

The reverse should be yellow on dark grey and will have the web address:
- harbourlinehandyworks.com.au

And a few key services he offers:
GENERAL REPAIRS
PAINTING/TILING/
PAVING &CONCRETING
PRESSURE WASHING
ON-SITE WELDING
DECKING ADDITIONS & REPAIRS
FENCING
FULL BOND CLEANING

This will be first time the logo has been printed so you will need to come up with the best CMYK approximation of the RGB colours to make sure it is a close as possible.

```html
<!DOCTYPE html>
<html lang="en">
<head>
<meta charset="utf-8">
<title>Harbourline Handyworks – Business Card</title>
<link rel="stylesheet" href="https://fonts.googleapis.com/css2?family=Open+Sans:ital,wght@0,400;0,700;1,400&family=PT+Sans+Narrow:wght@400;700&display=swap">
<style>
  :root {
    --card-yellow: #f2d31b;
    --card-charcoal: #262424;
    --backdrop: #e4e4e4;
    --backdrop-edge: #cfcfcf;
  }
  * { margin: 0; padding: 0; box-sizing: border-box; }
  html, body { width: 1034px; height: 1200px; overflow: hidden; }
  body {
    background: radial-gradient(ellipse at center, #f7f7f7 0%, var(--backdrop) 60%, var(--backdrop-edge) 100%);
    position: relative;
    font-family: "Open Sans", Arial, sans-serif;
  }
  .card {
    position: absolute;
    left: 160px;
    width: 707px;
    height: 404px;
  }
  .card--front { top: 135px; background: var(--card-charcoal); color: var(--card-yellow); }
  .card--back { top: 665px; background: var(--card-yellow); color: var(--card-charcoal); }

  .brand {
    position: absolute;
    left: 0; right: 0;
    text-align: center;
    font-family: "Open Sans", Arial, sans-serif;
    font-weight: 700;
    line-height: 1;
  }
  .card--front .brand { top: 62px; }
  .card--back .brand { top: 132px; }
  .brand__name { display: block; font-size: 86px; letter-spacing: -3px; }
  .brand__tagline { display: block; font-size: 23px; letter-spacing: 4px; margin-top: 14px; }

  .contact {
    position: absolute;
    left: 0; right: 0;
    top: 262px;
    text-align: center;
  }
  .contact__name { font-size: 27px; font-weight: 700; line-height: 1.2; }
  .contact__rule {
    width: 382px; height: 1.5px; margin: 8px auto 6px;
    background: var(--card-yellow);
  }
  .contact__line {
    font-family: "PT Sans Narrow", "Arial Narrow", sans-serif;
    font-size: 17px; line-height: 22px;
  }
  .contact__email { font-family: "Open Sans", Arial, sans-serif; font-style: italic; font-size: 15px; }
  .contact__label, .contact__insured { font-weight: 700; }

  .services {
    position: absolute;
    left: 0; right: 0;
    top: 340px;
    text-align: center;
    font-family: "PT Sans Narrow", "Arial Narrow", sans-serif;
    font-weight: 700;
    font-size: 16px;
    line-height: 25px;
    letter-spacing: -0.2px;
  }
</style>
</head>
<body>
  <section class="card card--front" aria-label="Card front">
    <div class="brand">
      <span class="brand__name">harbourline</span>
      <span class="brand__tagline">HANDYWORKS</span>
    </div>
    <div class="contact">
      <p class="contact__name">Warren Dobrinski</p>
      <div class="contact__rule"></div>
      <p class="contact__line contact__email">info@harbourlinehandyworks.com.au</p>
      <p class="contact__line"><span class="contact__label">Phone:</span> 0487.362.914; 0487.362.914</p>
      <p class="contact__line"><span class="contact__label">ABN:</span> 87 214 630 592 - <span class="contact__insured">'Fully Insured'</span></p>
    </div>
  </section>

  <section class="card card--back" aria-label="Card back">
    <div class="brand">
      <span class="brand__name">harbourline</span>
      <span class="brand__tagline">HANDYWORKS</span>
    </div>
    <div class="services">
      <p>GENERAL REPAIRS | PAINTING/TILING/ | PAVING &amp;CONCRETING | PRESSURE WASHING</p>
      <p>ON-SITE WELDING | DECKING ADDITIONS &amp; REPAIRS | FENCING | FULL BOND CLEANING</p>
    </div>
  </section>
</body>
</html>
```